Newspaper Ad

Please create an ad for a newspaper that is 10.5 wide and 13 inches long. Please highlight the features of the property and ensure that the name of our firm (Birchwood Hollow Realty) is the same size as our phone number which is 717-530-6198.

Pemberton's Crossing and The residences at 9 N. Ash
9 N. Ash Street, Quarryville PA

Now leasing 1, 2 & 3 bedroom units available this spring. Newley renovated apartments with stainless appliances, hardwood floors, granite countertops, in unit laundry. Includes water, sewer trash and off street parking. 1200sq first floor retail available.

717.530.6198 or www.BirchwoodHollowRealty.example for details.

```html
<!DOCTYPE html>
<html lang="en">
<head>
<meta charset="utf-8">
<title>Pemberton's Crossing – Newspaper Ad</title>
<link rel="stylesheet" href="https://fonts.googleapis.com/css2?family=Archivo:wght@400;800;900&family=Inter:wght@300;400&display=swap">
<style>
  :root {
    --page-bg: #dfe4ec;
    --sky-blue: #7a8db8;
    --sky-light: #c9d3e6;
    --ink-dark: #231f20;
    --band-blue: #7088b8;
    --card-white: #f2f2f2;
    --text-dark: #1c1a1b;
    --text-soft: #4a4a4a;
    --white: #ffffff;
  }
  * { box-sizing: border-box; margin: 0; padding: 0; }
  html, body {
    width: 1200px; height: 800px; overflow: hidden;
    background: var(--page-bg);
  }
  .ad {
    position: absolute; left: 285px; top: 10px;
    width: 630px; height: 780px;
    background: var(--ink-dark);
    overflow: hidden;
    font-family: "Inter", sans-serif;
  }
  .ad__photo {
    position: absolute; left: 0; top: 0; width: 630px; height: 470px;
    background: linear-gradient(180deg, var(--sky-blue) 0%, var(--sky-blue) 30%, var(--sky-light) 62%, #8a8f8c 78%, #4b4a48 100%);
  }
  .ad__headline {
    position: absolute; left: 34px; top: 30px; width: 560px;
    color: var(--white); font-weight: 300; font-size: 31px; line-height: 1.2;
  }
  .ad__address {
    margin-top: 8px;
    font-family: "Archivo", sans-serif; font-weight: 800;
    font-size: 17px; color: var(--text-dark);
  }
  .card {
    position: absolute; background: var(--card-white);
    border-radius: 12px; padding: 18px 20px; color: var(--text-dark);
  }
  .card__title {
    font-family: "Archivo", sans-serif; font-weight: 900;
    font-size: 22px; line-height: 1.1; letter-spacing: -0.3px;
  }
  .card__text { font-size: 14px; color: var(--text-soft); margin-top: 6px; line-height: 1.3; }
  .card--leasing { left: 36px; top: 470px; width: 215px; height: 108px; }
  .card--retail  { left: 36px; top: 590px; width: 215px; height: 90px; }
  .card--features { left: 266px; top: 470px; width: 330px; height: 210px; }
  .feature-list {
    list-style: none; display: grid; grid-template-columns: 1fr 1fr;
    column-gap: 10px; row-gap: 3px; margin-top: 8px;
    font-size: 13.5px; color: var(--text-soft);
  }
  .feature-list li::before { content: "\2713\00a0"; color: var(--text-dark); font-weight: 700; }
  .feature-list--includes { grid-template-columns: 1fr; }
  .card__subtitle {
    font-family: "Archivo", sans-serif; font-weight: 900;
    font-size: 17px; margin-top: 12px;
  }
  .includes { display: flex; gap: 40px; align-items: flex-start; }
  .includes .parking { margin-top: 36px; font-size: 13.5px; color: var(--text-soft); list-style: none; }
  .includes .parking li::before { content: "\2713\00a0"; color: var(--text-dark); font-weight: 700; }
  .band {
    position: absolute; left: 0; top: 700px; width: 630px; height: 56px;
    background: var(--band-blue);
    display: flex; align-items: center; justify-content: space-between;
    padding: 0 28px; color: var(--white);
    font-family: "Archivo", sans-serif; font-weight: 400; font-size: 27px;
    letter-spacing: 0.5px;
  }
  .footer-web {
    position: absolute; left: 28px; top: 760px;
    color: var(--white); font-size: 11px; letter-spacing: 0.3px;
  }
</style>
</head>
<body>
  <article class="ad">
    <div class="ad__photo" role="img" aria-label="Photo of the renovated three-storey corner building with porches under a blue sky with clouds"></div>
    <header class="ad__headline">
      <h1 style="font-weight:300;font-size:inherit;">Pemberton's Crossing<br>and The residences at 9 N. Ash</h1>
      <p class="ad__address">9 N. Ash Street, Quarryville PA</p>
    </header>

    <section class="card card--leasing">
      <h2 class="card__title">Now leasing</h2>
      <p class="card__text">1, 2 &amp; 3 bedroom units<br>available this spring.</p>
    </section>

    <section class="card card--retail">
      <h2 class="card__title">1200sq</h2>
      <p class="card__text">first floor retail available.</p>
    </section>

    <section class="card card--features">
      <h2 class="card__title" style="font-size:18px;">Newley renovated apartments with:</h2>
      <ul class="feature-list">
        <li>stainless appliances,</li>
        <li>granite countertops,</li>
        <li>hardwood floors,</li>
        <li>in unit laundry.</li>
      </ul>
      <div class="includes">
        <div>
          <h3 class="card__subtitle">Includes</h3>
          <ul class="feature-list feature-list--includes">
            <li>water,</li>
            <li>sewer trash,</li>
          </ul>
        </div>
        <ul class="parking"><li>off street parking.</li></ul>
      </div>
    </section>

    <footer>
      <div class="band">
        <span class="band__firm">Birchwood Hollow Realty</span>
        <span class="band__phone">717 530 6198</span>
      </div>
      <p class="footer-web">www.BirchwoodHollowRealty.example</p>
    </footer>
  </article>
</body>
</html>
```